RV Park - Advertising RV Park using Billboard 12 ft wide by 6 ft tall size

We need a sign for a relatively new RV Park called Bramblewood of Carver RV Park at 2745 Danbury Road, Murphy , NC. The sign should include our web address and phone number. bramblewoodcarverrv.example, 555-314-2967. We would like to see designs that include nice color and no tacky cartoons. Final design should communicate a nice and safe RV Park. We would also like to include quick directions - Just Ahead! Left on Kestrel Rd then left on Danbury Rd. (A nice motor home or RV representation may be nice but not mandatory to be included.) Classic but eye catching design. Sign is 12 ft wide by 6 ft tall in size. Will likely be vinyl printed.

```html
<!DOCTYPE html>
<html lang="en">
<head>
<meta charset="utf-8">
<title>Bramblewood of Carver RV Park – Billboard</title>
<link rel="stylesheet" href="https://fonts.googleapis.com/css2?family=Montserrat:wght@600;800;900&family=Mouse+Memoirs&family=Fredoka:wght@700&family=Cinzel:wght@500&display=swap">
<style>
  :root {
    --backdrop: #eef1f4;
    --black: #000000;
    --tan: #e3c08e;
    --cream: #fde7c8;
    --white: #ffffff;
    --blue: #0a72bb;
    --shadow-navy: #4a4f72;
    --red: #a01b22;
    --ink: #1b1b1b;
  }
  * { box-sizing: border-box; margin: 0; padding: 0; }
  html, body { width: 1200px; height: 1117px; overflow: hidden; background: var(--backdrop); }

  .billboard {
    position: absolute; left: 20px; top: 265px;
    width: 1160px; height: 586px;
    background: var(--black);
    overflow: hidden;
  }
  .panel {
    position: absolute; left: 12px; top: 12px; right: 12px; bottom: 12px;
    border: 5px solid var(--tan);
    border-radius: 38px;
    overflow: hidden;
    background: var(--black);
  }
  .rv-art {
    position: absolute; left: 520px; top: 20px; width: 620px; height: 200px;
    background: radial-gradient(ellipse at 40% 10%, #3a3a3a 0%, #000 40%),
                linear-gradient(90deg, transparent 0%, transparent 50%, #f4f4f4 51%, #ffffff 100%);
  }
  .rv-art::after {
    content: ""; position: absolute; left: 330px; top: 20px; width: 290px; height: 180px;
    background: linear-gradient(160deg, #e9e9e9, #1a1a1a 70%);
    border-radius: 30px 0 0 0;
  }
  .title {
    position: absolute; left: 78px; top: 46px;
    font-family: "Montserrat", sans-serif; font-weight: 800;
    font-size: 50px; line-height: 0.98; letter-spacing: 0.5px;
  }
  .title .line-1 { color: var(--white); display: block; }
  .title .line-2 { color: var(--cream); display: block; }

  .lower-white {
    position: absolute; left: 0; right: 0; top: 290px; bottom: 0;
    background: var(--white);
  }
  .directions {
    position: absolute; left: 70px; top: 313px;
    font-family: "Mouse Memoirs", sans-serif;
    font-size: 52px; color: var(--blue); letter-spacing: 0.5px;
    white-space: nowrap;
  }
  .footer {
    position: absolute; left: 0; right: 0; top: 376px; bottom: 0;
    background: var(--red);
  }
  .brand-box {
    position: absolute; left: 72px; top: 0; width: 357px; bottom: 0;
    background: var(--white);
    display: flex; align-items: center; justify-content: center;
  }
  .brand-name {
    font-family: "Cinzel", serif; font-weight: 500;
    font-size: 30px; line-height: 1.15; color: var(--ink);
    text-align: center; letter-spacing: 2px;
  }
  .contact {
    position: absolute; left: 429px; right: 0; top: 0; bottom: 0;
    display: flex; flex-direction: column; align-items: center; justify-content: center;
    padding-top: 4px;
  }
  .phone {
    display: flex; align-items: center; gap: 14px;
    font-family: "Fredoka", sans-serif; font-weight: 700;
    font-size: 70px; line-height: 1; color: var(--white); letter-spacing: -1px;
  }
  .phone-icon { width: 56px; height: 56px; flex: none; }
  .web {
    margin-top: 6px;
    font-family: "Montserrat", sans-serif; font-weight: 600;
    font-size: 25px; color: var(--white); letter-spacing: 8.5px;
  }

  .ahead-arrow { position: absolute; left: 0; top: 0; width: 1160px; height: 586px; }
  .ahead-text {
    position: absolute; left: 74px; top: 196px;
    font-family: "Montserrat", sans-serif; font-weight: 900;
    font-size: 96px; line-height: 1; color: var(--white);
    text-shadow: 6px 6px 0 var(--shadow-navy);
    letter-spacing: 1px; white-space: nowrap;
  }
</style>
</head>
<body>
<main class="billboard">
  <div class="panel">
    <div class="rv-art" role="img" aria-label="Illustration of a motor home"></div>
    <h1 class="title">
      <span class="line-1">BRAMBLEWOOD OF</span>
      <span class="line-2">CARVER RV PARK</span>
    </h1>
    <div class="lower-white"></div>
    <p class="directions">LEFT ON KESTREL RD THEN LEFT ON DANBURY RD.</p>
    <footer class="footer">
      <div class="brand-box">
        <p class="brand-name">BRAMBLEWOOD<br>OF CARVER</p>
      </div>
      <div class="contact">
        <p class="phone">
          <svg class="phone-icon" viewBox="0 0 56 56" aria-hidden="true">
            <circle cx="28" cy="28" r="28" fill="var(--tan)"/>
            <path d="M20 15c2-1 4 0 5 2l2 5c1 2 0 3-1 4l-2 2c1 3 4 6 7 7l2-2c1-1 2-2 4-1l5 2c2 1 3 3 2 5-1 3-4 5-7 4-10-2-18-10-20-20-1-3 1-7 3-8z" fill="var(--red)"/>
          </svg>
          555-314-2967
        </p>
        <p class="web">bramblewoodcarverrv.example</p>
      </div>
    </footer>
  </div>

  <svg class="ahead-arrow" viewBox="0 0 1160 586" aria-hidden="true">
    <path d="M0 208 H1020 V154 L1108 268 L1020 382 V328 H0 Z" fill="var(--blue)"/>
  </svg>
  <p class="ahead-text">JUST AHEAD!</p>
</main>
</body>
</html>
```